Prepared Meal Delivery Website

Need a new modern design for a prepared meal delivery company that is hosted on Shopify.

Target Market(s)

Young Professionals

Industry/Entity Type

Prepared Meal Delivery Service

Number of Pages Required

5+ page

Requirements
Must have
• Use https://www.velmorafoods.com/ as an example
Nice to have
• Vibrant page with call to action obvious and repeated
Should not have
• Generic look, grays/white/black

```html
<!DOCTYPE html>
<html lang="en">
<head>
<meta charset="utf-8">
<title>Hustle Plate Meals</title>
<link rel="stylesheet" href="https://fonts.googleapis.com/css2?family=Arimo:wght@400;700&family=Arvo:wght@400;700&display=swap">
<style>
:root{
  --orange:#f05a28;
  --navy:#243a51;
  --navy-deep:#1c2f43;
  --ink:#1f3246;
  --muted:#8d8d8d;
  --panel:#f2f2f2;
  --white:#ffffff;
}
*{box-sizing:border-box;margin:0;padding:0}
html,body{width:1200px;height:4309px;overflow:hidden}
body{position:relative;background:var(--white);font-family:"Arimo",Arial,sans-serif;color:var(--ink)}
.abs{position:absolute}
.btn{position:absolute;display:flex;align-items:center;justify-content:center;background:var(--orange);color:var(--white);font-weight:700;font-size:14px;border-radius:24px;text-decoration:none;letter-spacing:.2px}
.serif{font-family:"Arvo",Georgia,serif;font-weight:400}
.photo{position:absolute}

/* header */
.brand-mark{position:absolute;left:110px;top:13px;width:94px;height:94px;border:2px solid var(--ink);border-radius:50%;display:flex;align-items:center;justify-content:center;text-align:center;font-size:10px;font-weight:700;line-height:1.25;color:var(--ink)}
.nav{position:absolute;top:82px;left:0;width:1200px;font-size:15px;font-weight:700}
.nav a{position:absolute;color:var(--ink);text-decoration:none;white-space:nowrap}
.nav a.active{color:var(--orange)}
.head-icons{position:absolute;top:30px;left:814px;display:flex;gap:26px}

/* hero */
.hero-title{position:absolute;left:546px;top:292px;color:var(--white);font-size:40px;line-height:46px;letter-spacing:1px}
.foodies{position:absolute;left:924px;top:334px;color:var(--white);font-size:20px}

/* section titles */
.section-title{position:absolute;width:1200px;text-align:center;font-size:36px;color:var(--ink)}

/* step cards */
.step{position:absolute;top:807px;width:310px;height:433px;background:var(--white);box-shadow:0 2px 10px rgba(0,0,0,.16);border-radius:4px;text-align:center}
.step .photo{left:8px;top:8px;width:294px;height:199px}
.step h3{position:absolute;top:238px;width:100%;font-size:17px;letter-spacing:.5px}
.step p{position:absolute;top:270px;left:10px;width:290px;font-size:13.5px;line-height:24px;color:var(--muted)}
.step .btn{left:80px;top:365px;width:150px;height:46px}

/* audience */
.audience{position:absolute;top:1341px;left:0;width:1200px;height:616px;background:var(--panel)}
.aud-icon{position:absolute;left:110px;width:78px;height:78px;background:var(--white);border-radius:4px;box-shadow:0 1px 6px rgba(0,0,0,.08);display:flex;align-items:center;justify-content:center}
.aud-item h3{position:absolute;left:219px;font-size:17px;letter-spacing:.3px}
.aud-item p{position:absolute;left:219px;width:330px;font-size:14px;line-height:22.5px;color:var(--muted)}
.dish{position:absolute;width:234px;background:linear-gradient(135deg,#b9b7b4 0%,#d9d5cf 45%,#c49a74 70%,#a9a6a2 100%)}

/* about */
.about-text{position:absolute;left:653px;top:2201px;width:435px;font-size:14px;line-height:25px;color:var(--muted);text-align:justify}

/* standard */
.standard{position:absolute;top:2657px;left:0;width:1200px;height:512px;background:linear-gradient(100deg,#2b3d4f 0%,#384a58 45%,#5e6e55 75%,#8b5a3c 100%)}
.standard-text{position:absolute;left:110px;top:2814px;width:440px;color:var(--white);font-size:14.5px;line-height:25px;text-align:justify}
.who{position:absolute;top:3077px;width:232px;height:274px;background:var(--white);box-shadow:0 2px 10px rgba(0,0,0,.15);text-align:center}
.who .photo{left:8px;top:8px;width:216px;height:206px}
.who span{position:absolute;left:0;width:100%;top:236px;font-size:19px;font-weight:700;color:var(--ink)}

/* testimonial */
.quote{position:absolute;left:418px;top:3582px;width:670px;height:295px;background:var(--orange);color:var(--white)}
.quote p{position:absolute;left:42px;top:52px;width:586px;font-size:13.5px;line-height:24px;text-align:justify}
.quote strong{position:absolute;left:42px;top:218px;font-size:19px}
.dots{position:absolute;left:219px;top:3865px;display:flex;gap:7px}
.dots i{width:12px;height:12px;border:1.5px solid #7b8895;border-radius:50%}
.dots i.on{background:var(--orange);border-color:var(--orange)}

/* footer */
.footer{position:absolute;top:3982px;left:0;width:1200px;height:270px;background:var(--navy)}
.footer-bar{position:absolute;top:4252px;left:0;width:1200px;height:57px;background:var(--navy-deep);color:var(--white);text-align:center;font-size:13.5px;line-height:57px}
.foot-logo{position:absolute;left:112px;top:4039px;width:168px;height:168px;border:3px solid var(--white);border-radius:50%;display:flex;align-items:center;justify-content:center;text-align:center;color:var(--white);font-weight:700;font-size:16px;line-height:1.3}
.foot-h{position:absolute;top:4034px;color:var(--white);font-size:18px;font-weight:700}
.foot-links a{position:absolute;left:375px;color:var(--white);font-size:13px;text-decoration:none}
.foot-contact{position:absolute;left:590px;display:flex;align-items:center;gap:12px;color:var(--white);font-size:13.5px}
.ic{width:26px;height:26px;border-radius:50%;background:var(--orange);display:flex;align-items:center;justify-content:center}
.newsletter{position:absolute;left:837px;top:4088px;width:251px;height:34px;background:var(--white);border-radius:17px;overflow:hidden}
.newsletter span{position:absolute;left:16px;top:10px;font-size:11px;color:#777}
.newsletter b{position:absolute;right:0;top:0;width:50px;height:34px;background:var(--orange);display:flex;align-items:center;justify-content:center}
.social{position:absolute;top:4138px;left:839px;display:flex;gap:8px}
.social i{width:26px;height:26px;border-radius:50%;display:block}
.chat{position:absolute;left:1128px;top:4185px;width:40px;height:40px;border-radius:50%;background:var(--orange);display:flex;align-items:center;justify-content:center}
</style>
</head>
<body>

<header>
  <div class="brand-mark">Hustle<br>Plate<br>Meals</div>
  <div class="head-icons">
    <svg width="18" height="18" viewBox="0 0 18 18"><circle cx="7.5" cy="7.5" r="5.5" fill="none" stroke="#1f3246" stroke-width="2.2"/><line x1="11.5" y1="11.5" x2="16" y2="16" stroke="#1f3246" stroke-width="2.5"/></svg>
    <svg width="18" height="18" viewBox="0 0 18 18"><circle cx="9" cy="9" r="7.5" fill="none" stroke="#1f3246" stroke-width="2"/><circle cx="9" cy="7" r="2.6" fill="#1f3246"/><path d="M4.5 14c1.5-3 7.5-3 9 0" fill="#1f3246"/></svg>
    <svg width="18" height="18" viewBox="0 0 18 18"><path d="M1 2h3l2 9h9l2-6H5" fill="#1f3246" stroke="#1f3246" stroke-width="1.5"/><circle cx="7" cy="15" r="1.6" fill="#1f3246"/><circle cx="14" cy="15" r="1.6" fill="#1f3246"/></svg>
  </div>
  <a class="btn" style="left:956px;top:17px;width:132px;height:45px">SHOP NOW</a>
  <nav class="nav">
    <a class="active" style="left:348px">HOME</a>
    <a style="left:435px">BUSINESS PLAN</a>
    <a style="left:604px">ABOUT US</a>
    <a style="left:725px">GIFT CARDS</a>
    <a style="left:862px">REWARDS</a>
    <a style="left:981px">CONTACT US</a>
  </nav>
</header>

<section class="hero">
  <div class="photo" role="img" aria-label="Salad bowls on a table" style="left:0;top:119px;width:482px;height:514px;background:linear-gradient(135deg,#6d6a45,#b89a6a)"></div>
  <div class="photo" role="img" aria-label="Couple holding meal prep containers" style="left:47px;top:170px;width:435px;height:463px;background:linear-gradient(160deg,#cfc6bb,#e6ddd2 55%,#c9b8a6)"></div>
  <div class="photo" role="img" aria-label="Bowl of grilled tofu, broccoli and rice" style="left:482px;top:119px;width:414px;height:514px;background:linear-gradient(150deg,#5b5448,#8e6a45 45%,#b77a3f 75%,#6f7a4a)"></div>
  <h1 class="hero-title serif">EMPOWERING<br>EVERYONE</h1>
  <a class="btn" style="left:547px;top:407px;width:148px;height:42px;font-size:13px">ORDER NOW</a>
  <div class="photo" role="img" aria-label="Hands holding a meal container with corn salad" style="left:900px;top:119px;width:300px;height:261px;background:linear-gradient(135deg,#d9d2cc,#b7a089 60%,#a9744c)"></div>
  <span class="foodies serif">FOODIES</span>
  <div class="photo" role="img" aria-label="Fork lifting food over a plate" style="left:900px;top:385px;width:148px;height:248px;background:linear-gradient(180deg,#3a2e2a,#c9a552 60%,#b1475f)"></div>
  <div class="photo" role="img" aria-label="Woman holding a salad container" style="left:1053px;top:385px;width:147px;height:248px;background:linear-gradient(180deg,#c9d7d9,#8a6a57 55%,#b9c3b8)"></div>
</section>

<section>
  <h2 class="section-title serif" style="top:727px">WHAT WE DO</h2>
  <article class="step" style="left:110px">
    <div class="photo" role="img" aria-label="Plate of shrimp, potatoes and broccoli" style="background:linear-gradient(135deg,#6a6a6a,#a0764b 45%,#d8a763 70%,#5c5c5c)"></div>
    <h3>CHOOSE A PLAN</h3>
    <p>Choose one of our pre-set plans,<br>or Build Your Own!</p>
    <a class="btn">ORDER NOW</a>
  </article>
  <article class="step" style="left:445px">
    <div class="photo" role="img" aria-label="Packaged salad meal container" style="background:linear-gradient(180deg,#1d1d1d,#7f9c4a 55%,#2a2a2a)"></div>
    <h3>AWAIT DELIVERY</h3>
    <p>We deliver twice weekly, on Sundays &amp; Wednesdays Our delivery window is between 3 pm and 8 pm</p>
    <a class="btn">SHOP NOW</a>
  </article>
  <article class="step" style="left:780px">
    <div class="photo" role="img" aria-label="Woman heating a meal in the microwave" style="background:linear-gradient(135deg,#e4e1dc,#9fa3a6 55%,#c79e76)"></div>
    <h3>HEAT &amp; EAT</h3>
    <p>Place your meal in the microwave for 2-2.5 minutes or reheat to preferred temperature on a pan/skillet</p>
    <a class="btn">ORDER NOW</a>
  </article>
</section>

<section class="audience"></section>
<div class="aud-item">
  <div class="aud-icon" style="top:1401px"><svg width="40" height="40" viewBox="0 0 40 40" fill="none" stroke="#f05a28" stroke-width="2"><rect x="6" y="8" width="24" height="26" rx="2"/><line x1="11" y1="15" x2="25" y2="15"/><line x1="11" y1="21" x2="25" y2="21"/><line x1="11" y1="27" x2="19" y2="27"/><rect x="22" y="20" width="13" height="13" rx="2"/></svg></div>
  <h3 style="top:1397px">PROFESSIONALS</h3>
  <p style="top:1430px">HPM is the ideal service for the professional on the go. We deliver twice weekly so you can focus on your career and prioritize your business without compromising on nutrition.</p>
</div>
<div class="aud-item">
  <div class="aud-icon" style="top:1580px"><svg width="40" height="40" viewBox="0 0 40 40" fill="none" stroke="#f05a28" stroke-width="2"><circle cx="12" cy="13" r="4"/><circle cx="28" cy="13" r="4"/><circle cx="20" cy="24" r="3.5"/><path d="M5 30c0-6 14-6 14 0M21 30c0-6 14-6 14 0M14 36c0-5 12-5 12 0"/></svg></div>
  <h3 style="top:1576px">FAMILIES</h3>
  <p style="top:1609px">Set your family up for success with a week of healthy meals planned ahead. By ordering the week before, you'll be able to able to serve your family healthy meals with minimal effort!</p>
</div>
<div class="aud-item">
  <div class="aud-icon" style="top:1761px"><svg width="40" height="40" viewBox="0 0 40 40" fill="none" stroke="#f05a28" stroke-width="2"><circle cx="20" cy="13" r="5"/><path d="M10 34c0-10 20-10 20 0"/><path d="M5 12l4 4M35 12l-4 4M20 3v3"/></svg></div>
  <h3 style="top:1756px">SINGLES</h3>
  <p style="top:1789px">Cooking can be tiring and costly for individuals. Enjoy a clean fridge full of as many or as few meals as you need! No more wasted ingredients, just pure sustainable joy of eating!</p>
</div>
<h2 class="abs serif" style="left:606px;top:1393px;font-size:34px;line-height:41px">WHO IS HPM<br>FOR ?</h2>
<a class="btn" style="left:956px;top:1411px;width:132px;height:47px">SHOP NOW</a>
<div class="dish" role="img" aria-label="Plate of steak, green beans and rice" style="left:606px;top:1503px;height:191px"></div>
<div class="dish" role="img" aria-label="Plate of salmon and rice" style="left:854px;top:1503px;height:191px"></div>
<div class="dish" role="img" aria-label="Plate of chicken, asparagus and potatoes" style="left:606px;top:1709px;height:189px"></div>
<div class="dish" role="img" aria-label="Plate of salad and white rice" style="left:854px;top:1709px;height:189px"></div>

<section>
  <div class="photo" role="img" aria-label="Fresh vegetables and berries" style="left:110px;top:2064px;width:300px;height:368px;background:linear-gradient(160deg,#5d6b66,#2f3a2a 55%,#6b7e4f)"></div>
  <div class="abs" style="left:410px;top:2102px;width:64px;height:57px;background:var(--orange)"></div>
  <div class="abs" style="left:216px;top:2432px;width:57px;height:62px;background:var(--navy)"></div>
  <div class="photo" role="img" aria-label="Woman eating a meal at a table" style="left:273px;top:2165px;width:308px;height:369px;background:linear-gradient(170deg,#ece8e1,#c8a27e 55%,#7d5b42);border:6px solid #fff;"></div>
  <h2 class="abs serif" style="left:653px;top:2136px;font-size:36px">ABOUT HPM</h2>
  <p class="about-text">Let's be honest, it's not easy to eat healthily - it can take hours of planning, sourcing, cooking and cleaning to prepare a single nutritious and delicious meal (and that's assuming you can cook!). So with our increasingly busy lives, it's not surprising that fast food and unhealthy, processed, and packaged options easily become far too frequent occurrences.</p>
  <a class="btn" style="left:653px;top:2412px;width:139px;height:45px;font-size:13px">READ MORE</a>
</section>

<section class="standard" role="img" aria-label="Bowl of fresh chopped salad on a wooden table"></section>
<h2 class="abs serif" style="left:110px;top:2750px;font-size:36px;color:var(--white)">OUR STANDARD</h2>
<p class="standard-text">Our objective is to provide the freshest, most nourishing food possible. That means 100% commitment to safety and quality control practices in all the steps taken to prepare our meals, from farm to table.</p>
<a class="btn" style="left:110px;top:2950px;width:150px;height:45px;font-size:13px">ORDER NOW</a>
<div class="who" style="left:110px"><div class="photo" role="img" aria-label="Athlete holding a meal" style="background:linear-gradient(160deg,#d7cfc5,#8a6b58 55%,#a9b9c6)"></div><span>ATHLETES</span></div>
<div class="who" style="left:360px"><div class="photo" role="img" aria-label="Professional eating at a laptop" style="background:linear-gradient(160deg,#eeeae5,#d6c0a8 55%,#8a8d7f)"></div><span>PROFESSIONALS</span></div>
<div class="who" style="left:608px"><div class="photo" role="img" aria-label="Senior woman holding a meal" style="background:linear-gradient(160deg,#2e2e2e,#d3a98b 50%,#b6493a)"></div><span>SENIORS</span></div>
<div class="who" style="left:857px"><div class="photo" role="img" aria-label="Student eating on a couch" style="background:linear-gradient(160deg,#dedbd6,#7c8f9a 55%,#4e6170)"></div><span>STUDENTS</span></div>

<section>
  <h2 class="section-title serif" style="top:3440px">TESTIMONIALS</h2>
  <div class="photo" role="img" aria-label="Woman sitting with meal containers" style="left:110px;top:3542px;width:334px;height:286px;background:linear-gradient(150deg,#e9e5df,#5b6b52 45%,#d9c5b0)"></div>
  <div class="quote">
    <p>This meal service has been an absolute life saver!! They offer super healthy meals and we are really enjoying the low-carb option with lots of vegetables. This service is a huge time saver for our busy lifestyle and it will definitely assist with our weight loss goals. We also love that there is minimal waste. We have thoroughly enjoyed every meal that we have tried so far and we are satisfied with the portions. We will definitely be long-term customers. Thanks HPM!!</p>
    <strong>- MAREN</strong>
  </div>
  <div class="dots"><i></i><i></i><i class="on"></i><i></i></div>
</section>

<footer>
  <div class="footer"></div>
  <div class="foot-logo">Hustle<br>Plate<br>Meals</div>
  <div class="foot-h" style="left:369px">QUICK LINKS</div>
  <div class="foot-h" style="left:592px">CONTACT US</div>
  <div class="foot-h" style="left:837px">JOIN OUR COMMUNITY</div>
  <div class="foot-links">
    <a style="top:4084px">Business Plan</a>
    <a style="top:4112px">Gift Cards</a>
    <a style="top:4140px">Rewards</a>
    <a style="top:4168px">About Us</a>
    <a style="top:4196px">Contact Us</a>
  </div>
  <div class="foot-contact" style="top:4085px"><span class="ic"><svg width="13" height="13" viewBox="0 0 16 16"><path d="M3 1l3 3-2 2c1 2 3 4 5 5l2-2 3 3-2 3C7 15 1 9 1 3z" fill="#fff"/></svg></span>+1 (555) 014-2290</div>
  <div class="foot-contact" style="top:4138px"><span class="ic"><svg width="13" height="13" viewBox="0 0 16 16"><rect x="1" y="3" width="14" height="10" fill="#fff"/><path d="M1 3l7 6 7-6" fill="none" stroke="#f05a28" stroke-width="1.5"/></svg></span>hello@hustleplate.com</div>
  <div class="newsletter"><span>✉ Email Address</span><b><svg width="16" height="16" viewBox="0 0 16 16"><path d="M1 8l14-6-5 13-2-5z" fill="#fff"/></svg></b></div>
  <div class="social"><i style="background:var(--orange)"></i><i style="background:var(--white)"></i><i style="background:var(--white)"></i></div>
  <div class="chat"><svg width="20" height="20" viewBox="0 0 20 20"><path d="M10 3c4.5 0 8 2.8 8 6.3s-3.5 6.2-8 6.2c-1 0-2-.1-2.8-.4L3 17l1.2-3.4C2.8 12.5 2 11 2 9.3 2 5.8 5.5 3 10 3z" fill="#fff"/></svg></div>
  <div class="footer-bar">© 2022, HPM Meals All Rights Reserved.</div>
</footer>

</body>
</html>
```